Birch Flooring Supply

Basic one-sided business card design using the attached logo. Vintage americana theme. Font is modified Arial Nova Cond, but anything that coordinates can be used

```html
<!DOCTYPE html>
<html lang="en">
<head>
<meta charset="utf-8">
<title>Birch Flooring Supply – Business Card</title>
<link rel="stylesheet" href="https://fonts.googleapis.com/css2?family=Arimo:wght@400;700&display=swap">
<style>
  :root {
    --backdrop: #1d1d1d;
    --card-white: #ffffff;
    --panel-dark: #141414;
    --accent-gold: #b5976f;
    --ink: #2b2b2b;
    --logo-white: #ffffff;
  }
  * { margin: 0; padding: 0; box-sizing: border-box; }
  html, body {
    width: 1200px;
    height: 1059px;
    overflow: hidden;
    background: var(--backdrop);
    font-family: "Arimo", Arial, sans-serif;
  }
  .business-card {
    position: absolute;
    left: 190px;
    top: 296px;
    width: 821px;
    height: 468px;
    border-radius: 24px;
    background: var(--card-white);
    overflow: hidden;
  }
  .brand-panel {
    position: absolute;
    inset: 0;
    width: 821px;
    height: 468px;
  }
  .brand-panel path { fill: var(--panel-dark); }
  .name-marker {
    position: absolute;
    left: 0;
    top: 61px;
    width: 19px;
    height: 61px;
    background: var(--accent-gold);
  }
  .person-name {
    position: absolute;
    left: 35px;
    top: 52px;
    font-size: 38px;
    font-weight: 700;
    color: var(--accent-gold);
    letter-spacing: 0.2px;
    line-height: 1;
  }
  .person-title {
    position: absolute;
    left: 35px;
    top: 98px;
    font-size: 22px;
    color: var(--ink);
    line-height: 1;
  }
  .address {
    position: absolute;
    left: 38px;
    top: 191px;
    font-size: 22px;
    color: var(--ink);
    line-height: 33px;
  }
  .contact-list {
    position: absolute;
    left: 38px;
    top: 315px;
    list-style: none;
  }
  .contact-item {
    display: flex;
    align-items: center;
    height: 33px;
    font-size: 22px;
    color: var(--ink);
  }
  .contact-icon {
    width: 18px;
    height: 18px;
    margin-right: 11px;
    flex: none;
  }
  .contact-icon * { fill: var(--accent-gold); }
  .brand-name {
    position: absolute;
    left: 448px;
    top: 234px;
    width: 300px;
    transform: translateY(-50%);
    text-align: center;
    font-weight: 700;
    font-size: 34px;
    line-height: 1.15;
    color: var(--logo-white);
    letter-spacing: 1px;
  }
</style>
</head>
<body>
  <div class="business-card">
    <svg class="brand-panel" viewBox="0 0 821 468" aria-hidden="true">
      <path d="M575 0 A221 234 0 0 0 575 468 L821 468 L821 0 Z"/>
    </svg>

    <div class="name-marker"></div>
    <h1 class="person-name">DANIEL HAYES</h1>
    <p class="person-title">Managing Director</p>

    <p class="address">Your address, City<br>State, Zip 1234</p>

    <ul class="contact-list">
      <li class="contact-item">
        <svg class="contact-icon" viewBox="0 0 18 18" aria-hidden="true">
          <path d="M1 6 Q9 1 17 6 L15 8 L12 6.5 L12 5 Q9 4 6 5 L6 6.5 L3 8 Z"/>
          <rect x="3" y="9" width="12" height="7" rx="1"/>
        </svg>
        <span>123 456 789</span>
      </li>
      <li class="contact-item">
        <svg class="contact-icon" viewBox="0 0 18 18" aria-hidden="true">
          <path d="M1 7 L9 2 L17 7 L17 16 L1 16 Z M2.5 8 L9 12.5 L15.5 8 L15.5 7.6 L9 3.8 L2.5 7.6 Z"/>
        </svg>
        <span>info@birchfloorco.com</span>
      </li>
      <li class="contact-item">
        <svg class="contact-icon" viewBox="0 0 18 18" aria-hidden="true">
          <path d="M9 1 A8 8 0 1 0 9.01 1 Z M9 2.6 A6.4 6.4 0 0 1 15 7 L12 7.5 L11 5.5 L8 6 L7 9 L9.5 11 L8.5 15.3 A6.4 6.4 0 0 1 4 4.5 L6 5 L7.5 3 Z"/>
        </svg>
        <span>www.birchfloorco.com</span>
      </li>
    </ul>

    <p class="brand-name">BIRCH<br>FLOORING SUPPLY</p>
  </div>
</body>
</html>
```